Design concept for PixelHarbor.com Support Page

We are about to launch a new support page for our www.pixelharbor.example service for photographers and visual artists. The service provides media management, cloud storage, promotional and secure distribution to our members.

The support page will include FAQs and video tutorials.

In particular we're looking for a header for this page that suggests the user is in the support area of our service - so perhaps an illustration that suggests support could look nice (perhaps repair man or doctor iconography). Something to give this area of our site a different look and something that looks both cool and friendly.

Currently the page looks distinctly sparse and undesigned (see attached screenshot) - something that could be remedied, we feel, by some subtle design enhancements that we can implement using CSS.

```html
<!DOCTYPE html>
<html lang="en">
<head>
<meta charset="utf-8">
<title>PixelHarbor Support – FAQ Page Design</title>
<link rel="stylesheet" href="https://fonts.googleapis.com/css2?family=Arimo:wght@400;700&family=Open+Sans:wght@400;700&family=Titillium+Web:wght@300;400;700&display=swap">
<style>
  :root{
    --red:#e8262a;
    --ink:#222;
    --muted:#555;
    --note:#4a4a4a;
    --green:#5aab26;
    --panel:#ededed;
    --rule:#e6e6e6;
    --footer:#000;
    --footer-link:#b5b5b5;
    --white:#fff;
  }
  *{margin:0;padding:0;box-sizing:border-box}
  html,body{width:1200px;height:1000px;overflow:hidden;background:var(--white)}
  body{position:relative;font-family:"Arimo",Arial,sans-serif;color:var(--ink)}
  .abs{position:absolute}

  /* page mock */
  .page{position:absolute;left:35px;top:0;width:749px;height:1000px;border-left:1px solid var(--rule);border-right:1px solid var(--rule);background:var(--white)}
  .hero{position:absolute;left:0;top:0;width:749px;height:145px;background:radial-gradient(ellipse at 60% 40%,#6d6d6d 0%,#3b3b3b 45%,#1c1c1c 100%)}
  .brand{position:absolute;left:95px;top:8px;display:flex;align-items:center;gap:6px;color:var(--white);font-family:"Open Sans",sans-serif;font-weight:700;font-size:19px;letter-spacing:-.3px}
  .brand-mark{width:15px;height:15px;border:2px solid var(--white);border-radius:3px}
  .hero-title{position:absolute;left:284px;top:57px;display:flex;gap:10px;color:var(--white)}
  .hero-title h1{font-family:"Open Sans",sans-serif;font-weight:700;font-size:16px;line-height:20px;letter-spacing:.1px}
  .hero-title p{font-size:14px;line-height:18px}

  .search{position:absolute;left:191px;top:177px;display:flex;height:31px}
  .search-input{width:297px;border:1px solid #ddd;border-right:none;font-size:11px;color:#b5b5b5;padding:8px 6px}
  .search-btn{width:70px;background:var(--red);color:var(--white);font-weight:700;font-size:11px;display:flex;align-items:center;justify-content:center;border:1px solid #c81e22}
  .divider{position:absolute;left:95px;top:238px;width:558px;height:1px;background:var(--rule)}

  .section-title{color:var(--red);font-size:18px;font-weight:400;position:absolute}
  .faq-list{position:absolute;left:95px;list-style:none;font-family:"Open Sans",sans-serif;font-weight:700;font-size:9.6px;line-height:14.3px;color:var(--ink)}
  .faq-list li::before{content:"+";color:var(--red);font-size:14px;font-weight:700;margin-right:3px;line-height:10px}
  .answer{position:absolute;left:95px;top:338px;width:324px;height:72px;background:var(--panel);border-radius:3px;padding:13px 11px;font-size:9.3px;line-height:11.3px;color:#444}
  .answer::before{content:"";position:absolute;left:20px;top:-7px;border:7px solid transparent;border-top:none;border-bottom-color:var(--panel)}

  .video-label{position:absolute;left:475px;font-size:9.5px;color:#555}
  .thumb{position:absolute;left:476px;width:130px;height:67px;display:flex;align-items:center;justify-content:center}
  .thumb-forest{background:linear-gradient(135deg,#4a5a3a,#2d3a22 55%,#6f7a62)}
  .thumb-beach{background:linear-gradient(180deg,#e8a08a 0%,#d97a6a 45%,#b78a6c 70%,#8a6a52 100%)}
  .thumb-hands{background:linear-gradient(135deg,#2b3f5c,#1c2a3d 55%,#7a6a58)}

  .help{position:absolute;left:0;top:672px;width:749px;text-align:center}
  .help h2{color:var(--red);font-size:18px;font-weight:400}
  .help p{font-size:10.5px;line-height:15px;color:#444;margin-top:6px}
  .contact-btn{position:absolute;left:290px;top:790px;width:168px;height:30px;background:var(--red);color:var(--white);font-weight:700;font-size:11px;display:flex;align-items:center;justify-content:center;border:1px solid #c81e22}

  .footer{position:absolute;left:0;top:911px;width:749px;height:89px;background:var(--footer);text-align:center;font-family:"Open Sans",sans-serif}
  .footer-nav{margin-top:21px;font-size:9.5px;color:var(--footer-link)}
  .footer-nav span{margin:0 2px}
  .footer-nav .dot{color:#888}
  .copyright{margin-top:13px;color:var(--white);font-size:9.3px}
  .powered{color:#8a8a8a;font-size:9.3px;margin-top:1px}

  /* presentation notes */
  .notes{position:absolute;left:845px;top:0;width:340px;font-family:"Titillium Web",sans-serif;color:var(--note)}
  .notes h1{position:absolute;top:17px;font-weight:400;font-size:23px;color:#444}
  .notes p{position:absolute;font-weight:300;font-size:15px;line-height:19px;width:330px}
  .notes .cta{position:absolute;color:var(--green);font-weight:700}
</style>
</head>
<body>

<main class="page">
  <header class="hero" role="img" aria-label="Blurred black and white photo of a photographer holding a camera">
    <div class="brand"><span class="brand-mark"></span>PixelHarbor</div>
    <div class="hero-title">
      <svg width="36" height="36" viewBox="0 0 36 36" aria-hidden="true">
        <path d="M27 3a8 8 0 0 0-8 10L4 28a3 3 0 0 0 4 4l15-15a8 8 0 0 0 10-8l-5 4-4-1-1-4 5-5z" fill="#fff"/>
        <circle cx="7" cy="29" r="1.5" fill="#3b3b3b"/>
      </svg>
      <div>
        <h1>PIXELHARBOR SUPPORT</h1>
        <p>We are happy to help...</p>
      </div>
    </div>
  </header>

  <form class="search">
    <div class="search-input">What are you looking for?</div>
    <div class="search-btn">SEARCH</div>
  </form>
  <div class="divider"></div>

  <h2 class="section-title" style="left:95px;top:278px">Frequently Asked Questions</h2>
  <h2 class="section-title" style="left:481px;top:277px">Video Tutorials</h2>

  <ul class="faq-list" style="top:313px">
    <li>Under Which License I can Use Other Photos?</li>
  </ul>
  <div class="answer">Lorem ipsum dolor sit amet, consectetur adipiscing elit. Etiam dignissim ullamcorper ipsum et mollis. Fusce eget massa lobortis nunc pulvinar aliquam. Lorem ipsum dolor sit amet, consectetur adipiscing elit. Etiam dignissim ullamcorper ipsum et mollis. Fusce eget massa lobortis nunc</div>
  <ul class="faq-list" style="top:427px">
    <li>How Can I Register?</li>
    <li>How Can I Delete My Account?</li>
    <li>How Can I send private message?</li>
    <li>Do I Need My Credit Card Details To register?</li>
    <li>How Can I Upload My Photos?</li>
    <li>How Can I Register?</li>
    <li>How Can I Delete My Account?</li>
    <li>How Can I send private message?</li>
    <li>Do I Need My Credit Card Details To register?</li>
    <li>How Can I Upload My Photos?</li>
    <li>How Can I Delete My Account?</li>
    <li>How Can I send private message?</li>
    <li>Do I Need My Credit Card Details To register?</li>
  </ul>

  <span class="video-label" style="top:313px">Register an account</span>
  <div class="thumb thumb-forest" style="top:333px" role="img" aria-label="Video thumbnail: photographer in a mossy forest">
    <svg width="26" height="26" viewBox="0 0 26 26" aria-hidden="true"><circle cx="13" cy="13" r="11" fill="none" stroke="#fff" stroke-width="2.5"/><path d="M10 8l8 5-8 5z" fill="#fff"/></svg>
  </div>
  <span class="video-label" style="top:420px">Sending Private Messages</span>
  <div class="thumb thumb-beach" style="top:440px" role="img" aria-label="Video thumbnail: lifeguard tower on a beach at sunset">
    <svg width="26" height="26" viewBox="0 0 26 26" aria-hidden="true"><circle cx="13" cy="13" r="11" fill="none" stroke="#fff" stroke-width="2.5"/><path d="M10 8l8 5-8 5z" fill="#fff"/></svg>
  </div>
  <span class="video-label" style="top:527px">Upload Photos</span>
  <div class="thumb thumb-hands" style="top:546px" role="img" aria-label="Video thumbnail: hands holding a camera">
    <svg width="26" height="26" viewBox="0 0 26 26" aria-hidden="true"><circle cx="13" cy="13" r="11" fill="none" stroke="#fff" stroke-width="2.5"/><path d="M10 8l8 5-8 5z" fill="#fff"/></svg>
  </div>

  <section class="help">
    <h2>Can’t Find What You Are Looking For?</h2>
    <p>Lorem ipsum dolor sit amet, consectetur adipiscing elit. Etiam<br>dignissim ullamcorper ipsum et mollis.</p>
  </section>
  <a class="contact-btn">CONTACT SUPPORT</a>

  <footer class="footer">
    <nav class="footer-nav">
      <span>Home</span><span class="dot">●</span><span>Contact Us</span><span class="dot">●</span><span>Affiliate Program</span><span class="dot">●</span><span>Privacy Policy</span><span class="dot">●</span><span>Site Terms and Conditions</span><span class="dot">●</span><span>About Us</span>
    </nav>
    <p class="copyright">© Copyright 2014 Harborline Media Pte Ltd. All rights reserved.</p>
    <p class="powered">Powered by PixelHarbor</p>
  </footer>
</main>

<aside class="notes">
  <h1>FAQ Page Design</h1>
  <p style="top:111px">The page is designed with the user in mind. The overall look is simple, user friendly.</p>
  <p style="top:165px">Notice the big Search form at the top. This will help users to quickly search within the FAQ questions and videos.</p>
  <p style="top:242px">The question are higlighted with bold text after a red cross. It should be clickable and the answer should slide down.</p>
  <p style="top:318px">The video tutorials, are in the right hand side. Each video should display a thumnail image. Clicking on the thumnails, a pop up window should open with the actual video.</p>
  <p style="top:414px">if more video will be placed on the site, a scrollbar will display so user can scroll up &amp; down to pick a video. Same can be used with the questions.</p>
  <p style="top:511px">If user not find the answer to hes/her question a button will be displayed just before the footer which redirects user to the contact page.</p>
  <span class="cta" style="top:607px;font-size:17px">PLEASE FEEL FREE TO CONTACT ME!</span>
  <p style="top:664px">If you have any questions, or would like to try some ideas out, please let me know. I’m here to solve problems.</p>
  <span class="cta" style="top:755px;font-size:22px">THANK YOU!</span>
</aside>

</body>
</html>
```